Kestrel Schools Vinyl Banner

Based on the attached images design a image that we will be printed onto a vinyl Banner and used at conventions.

Design liberties are welcome but it needs to look good and the the final submission will need to be submitted in .psd format with all layers being able to be edited.

Make it look good and atract new business

```html
<!DOCTYPE html>
<html lang="en">
<head>
<meta charset="utf-8">
<title>Kestrel Schools Vinyl Banner</title>
<link rel="stylesheet" href="https://fonts.googleapis.com/css2?family=Open+Sans:wght@600;700&family=Montserrat:ital,wght@1,500&display=swap">
<style>
  :root {
    --stage: #232323;
    --paper: #ffffff;
    --brand-blue: #1f5f99;
    --sky-blue: #2a8cc4;
    --mid-blue: #1a5aa6;
    --navy: #0f1f6e;
    --ink: #0a0a0a;
  }
  * { margin: 0; padding: 0; box-sizing: border-box; }
  html, body {
    width: 1200px; height: 1200px; overflow: hidden;
    background: var(--stage);
  }
  .banner {
    position: absolute; left: 72px; top: 380px;
    width: 1056px; height: 440px;
    background: var(--paper); overflow: hidden;
  }
  .brand {
    position: absolute; left: 38px; top: 26px;
    display: flex; align-items: center; gap: 24px;
  }
  .brand-dot {
    width: 62px; height: 62px; border-radius: 50%;
    background: var(--brand-blue);
  }
  .brand-name {
    font-family: "Open Sans", sans-serif; font-weight: 600;
    font-size: 31px; line-height: 35px; letter-spacing: 2px;
    color: var(--brand-blue); text-transform: uppercase;
  }
  .headline {
    position: absolute; left: 426px; top: 16px;
    font-family: "Open Sans", sans-serif; font-weight: 700;
    font-size: 60px; line-height: 57px; letter-spacing: -1.5px;
    color: var(--brand-blue); text-transform: uppercase;
  }
  .event {
    position: absolute; left: 428px; top: 140px;
    font-family: "Montserrat", sans-serif; font-style: italic; font-weight: 500;
    font-size: 49px; line-height: 58px; color: var(--ink);
  }
  .phone {
    position: absolute; left: 432px; top: 202px;
    display: flex; align-items: center; gap: 14px;
    font-family: "Open Sans", sans-serif; font-weight: 700;
    font-size: 31px; line-height: 40px; color: var(--ink);
  }
  .phone svg { width: 26px; height: 26px; }
  .graduate-art {
    position: absolute; left: 28px; top: 116px;
    width: 276px; height: 310px; border-radius: 14px;
    background: linear-gradient(180deg, var(--sky-blue) 0%, #2279b8 60%, var(--mid-blue) 100%);
  }
  .skyline-art {
    position: absolute; left: 0; right: 0; bottom: 0; height: 200px;
    background: linear-gradient(180deg,
      rgba(26, 90, 166, 0) 0%,
      rgba(26, 90, 166, 0.55) 30%,
      var(--mid-blue) 55%,
      var(--navy) 100%);
  }
  .web {
    position: absolute; left: 0; right: 0; top: 380px;
    text-align: center;
    font-family: "Open Sans", sans-serif; font-weight: 700;
    font-size: 24px; letter-spacing: 6px; color: var(--paper);
  }
</style>
</head>
<body>
  <main class="banner">
    <div class="graduate-art" role="img" aria-label="Illustration of a graduate silhouette wearing a mortarboard cap"></div>
    <div class="skyline-art" role="img" aria-label="Illustrated city skyline silhouette with towers across the bottom of the banner"></div>

    <div class="brand">
      <span class="brand-dot"></span>
      <span class="brand-name">Kestrel<br>Schools</span>
    </div>

    <h1 class="headline">Welcome to<br>Kestrel Schools</h1>
    <p class="event">Convocation in - 2018</p>
    <p class="phone">
      <svg viewBox="0 0 24 24" aria-hidden="true">
        <circle cx="12" cy="12" r="10.5" fill="none" stroke="currentColor" stroke-width="2"/>
        <path d="M8.6 6.8l1.6 2.4-1 1.2c.7 1.6 2 2.9 3.6 3.6l1.2-1 2.4 1.6-.8 1.9c-4.2-.3-8.6-4.7-8.9-8.9z" fill="currentColor"/>
      </svg>
      03 9555 0182
    </p>

    <p class="web">www.kestrelschools.com.au</p>
  </main>
</body>
</html>
```